Birchwell Landing - Multifamily Development

Birchwell Landing is a Luxury Multifamily Development project located in Orange, NJ. This project will be completed in three phases with the first phase about 75% complete. Each phase will have a different name as follows
CREST Birchwell Landing
RIDGE Birchwell Landing
ZENITHAL Birchwell Landing
We are going to install a banner on the side of the first building which will act as advertising for all buildings. We will eventually need advertising that will be in the windows as well as marketing materials . We want the marketing for this project to be similar for all three phases. At the moment, we are starting with this first simple banner. Attached is a rough idea of the look as well as our color palette. If you feel the color palette is a little too monochrome, feel free to propose an accent color. You can also visit our website to see more info on our company as well as the project. www.tolvarhq.com Finally, if you need AI files (ie. for the logo), we can send to you. Thanks..

```html
<!DOCTYPE html>
<html lang="en">
<head>
<meta charset="utf-8">
<title>CREST Birchwell Landing – Vertical Banner</title>
<link rel="stylesheet" href="https://fonts.googleapis.com/css2?family=Montserrat:ital,wght@0,600;0,700;0,800;1,900&display=swap">
<style>
  :root {
    --navy: #2f3a5a;
    --brand-blue: #3e64a6;
    --photo-blue-light: #6485bf;
    --photo-blue-mid: #4569aa;
    --photo-blue-dark: #2c4f8f;
    --white: #ffffff;
  }
  * { margin: 0; padding: 0; box-sizing: border-box; }
  html, body {
    width: 1200px;
    height: 3128px;
    overflow: hidden;
    background: var(--white);
  }
  .banner {
    position: relative;
    width: 1200px;
    height: 3128px;
    background: var(--white);
    font-family: "Montserrat", Arial, sans-serif;
    color: var(--navy);
  }
  .brand-name {
    position: absolute;
    top: 190px;
    left: 0;
    width: 100%;
    text-align: center;
    font-weight: 800;
    color: var(--navy);
    line-height: 1;
  }
  .brand-name__main {
    display: block;
    font-size: 220px;
    letter-spacing: 4px;
  }
  .brand-name__sub {
    display: block;
    margin-top: 30px;
    font-size: 76px;
    letter-spacing: 24px;
    padding-left: 24px;
  }
  .phase-title {
    position: absolute;
    top: 560px;
    left: 0;
    width: 100%;
    text-align: center;
    line-height: 1;
  }
  .phase-title__name {
    display: block;
    font-size: 140px;
    font-weight: 800;
    color: var(--brand-blue);
    letter-spacing: 3px;
  }
  .phase-title__place {
    display: block;
    margin-top: 28px;
    font-size: 86px;
    font-weight: 600;
    color: var(--navy);
    letter-spacing: 1px;
  }
  .roof-chevron {
    position: absolute;
    top: 830px;
    left: 0;
    width: 1200px;
    height: 220px;
  }
  .hero {
    position: absolute;
    top: 900px;
    left: 0;
    width: 1200px;
    height: 1850px;
    overflow: hidden;
    clip-path: polygon(0 170px, 50% 40px, 100% 170px, 100% 100%, 0 100%);
    background:
      linear-gradient(90deg, rgba(30,55,105,0.35) 0%, rgba(30,55,105,0) 40%, rgba(30,55,105,0) 70%, rgba(30,55,105,0.3) 100%),
      linear-gradient(170deg, var(--photo-blue-light) 0%, var(--photo-blue-mid) 45%, var(--photo-blue-dark) 100%);
  }
  .tagline {
    position: absolute;
    left: 0;
    top: 1850px;
    width: 1850px;
    height: 1200px;
    transform-origin: 0 0;
    transform: rotate(-90deg);
    padding-top: 335px;
    text-align: center;
    color: var(--white);
    font-style: italic;
    font-weight: 900;
    font-size: 124px;
    line-height: 290px;
    letter-spacing: 2px;
  }
  .tagline span { display: block; }
  .web-pill {
    position: absolute;
    top: 2830px;
    left: 50%;
    transform: translateX(-50%);
    padding: 8px 70px 16px;
    border: 8px solid var(--navy);
    border-radius: 80px;
    font-size: 88px;
    font-weight: 700;
    color: var(--navy);
    line-height: 1.1;
    white-space: nowrap;
  }
  .phone {
    position: absolute;
    top: 2980px;
    left: 0;
    width: 100%;
    text-align: center;
    font-size: 124px;
    font-weight: 800;
    color: var(--navy);
    letter-spacing: 2px;
    line-height: 1;
  }
</style>
</head>
<body>
  <main class="banner">
    <header class="brand-name">
      <span class="brand-name__main">TOLVAR</span>
      <span class="brand-name__sub">PROPERTIES</span>
    </header>

    <h1 class="phase-title">
      <span class="phase-title__name">CREST</span>
      <span class="phase-title__place">BIRCHWELL LANDING</span>
    </h1>

    <svg class="roof-chevron" viewBox="0 0 1200 220" aria-hidden="true">
      <polygon points="40,200 600,40 1160,200 1160,216 600,78 40,216" fill="var(--navy)"/>
    </svg>

    <section class="hero" role="img" aria-label="Photo of the apartment building facade in blue duotone">
      <p class="tagline">
        <span>LUXURY APARTMENT</span>
        <span>RENTALS</span>
      </p>
    </section>

    <p class="web-pill">tolvarhq.com</p>
    <p class="phone">555-014-2870</p>
  </main>
</body>
</html>
```